Verpackungen für ein CBD Öl
Zielgruppe
Wir bringen ein neues CBD Öl auf den Markt. Unsere Zielgruppe sind Männer und Frauen ab 18 Jahren die natürliche Produkte den 'Chemischen' bevorzugen.
Aufgabenstellung
Es soll bitte eine Faltschachteln für ein CBD Öl designt werden. Die Stanzvorlage habe ich hochgeladen. Als Name des CBD Öls bitte erstmal 'XX' nehmen. Wir werden den Namen zu einem späteren Zeitpunkt nennen. Wichtig ist, dass das Design modern und eher 'edel' aussieht.
Die Pflichttexte, Namen, Barcode etc. können zu einem späteren Zeitpunkt hinzugefügt werden.
Es geht erstmal nur um ein schönes Design :-)

```html
<!DOCTYPE html>
<html lang="de">
<head>
<meta charset="utf-8">
<title>XX Mundöl – Faltschachtel</title>
<link rel="stylesheet" href="https://fonts.googleapis.com/css2?family=Source+Sans+3:wght@400;600&display=swap">
<style>
  :root {
    --paper: #ffffff;
    --ink: #111111;
    --dieline: #8a8a8a;
    --leaf-green: #3aaa47;
    --photo-dark: #3f5a3a;
    --photo-mid: #7fa06e;
    --photo-light: #c7d9bb;
    --on-photo: #ffffff;
  }
  * { box-sizing: border-box; margin: 0; padding: 0; }
  html, body { width: 1200px; height: 675px; overflow: hidden; background: var(--paper); }
  body { position: relative; font-family: "Source Sans 3", "Myriad Pro", sans-serif; color: var(--ink); }

  .dieline-panel { position: absolute; border: 0.6px solid var(--dieline); }
  .flap-top { left: 708px; top: 76px; width: 113px; height: 110px; display: flex; align-items: center; justify-content: center; }
  .flap-top .brand { font-size: 40px; font-weight: 400; letter-spacing: -1px; line-height: 1; margin-top: -4px; }
  .flap-bottom { left: 481px; top: 522px; width: 113px; height: 110px; }

  .box-body { position: absolute; left: 370px; top: 186px; width: 451px; height: 336px; }
  .box-art { position: absolute; inset: 0; }

  .side-panel { position: absolute; top: 0; height: 336px; border: 0.6px solid var(--dieline); }
  .panel-usage { left: 0; width: 111px; }
  .panel-info { left: 111px; width: 113px; }
  .panel-front { left: 224px; width: 114px; border-color: transparent; }
  .panel-back { left: 338px; width: 113px; border-color: transparent transparent transparent var(--dieline); }

  .fine-print { position: absolute; top: 60px; font-size: 6.6px; line-height: 9px; letter-spacing: -0.05px; white-space: nowrap; }
  .fine-print p + p { margin-top: 9px; }
  .panel-usage .fine-print { left: 6px; }
  .panel-info .fine-print { left: 8px; }

  .barcode-slot { position: absolute; left: 8px; top: 271px; width: 96px; height: 34px; border: 0.8px solid var(--ink); display: flex; align-items: center; justify-content: center; font-size: 20px; font-weight: 600; letter-spacing: -0.3px; background: var(--paper); }

  .front-title { position: absolute; left: 0; right: 0; top: 50px; text-align: center; }
  .front-title .brand { font-size: 20px; line-height: 1; margin-left: 6px; }
  .front-title .claim { margin-top: 24px; font-size: 16px; line-height: 19.6px; }

  .panel-back .fine-print { left: 6px; top: 55px; color: var(--on-photo); }
</style>
</head>
<body>
  <div class="dieline-panel flap-top"><span class="brand">XX</span></div>
  <div class="dieline-panel flap-bottom"></div>

  <div class="box-body">
    <svg class="box-art" width="451" height="336" viewBox="0 0 451 336">
      <defs>
        <linearGradient id="hempFoliage" x1="0" y1="0" x2="1" y2="1">
          <stop offset="0" stop-color="var(--photo-light)"/>
          <stop offset="0.45" stop-color="var(--photo-mid)"/>
          <stop offset="1" stop-color="var(--photo-dark)"/>
        </linearGradient>
      </defs>
      <path role="img" aria-label="Foto: Nahaufnahme grüner Hanfblätter"
            d="M264,0 L451,0 L451,336 L114,336 C240,310 336,240 337,150 C338,80 300,25 264,0 Z"
            fill="url(#hempFoliage)"/>
      <path d="M264,0 C300,25 338,80 337,150 C336,240 240,310 114,336 L132,336 C236,306 330,238 330,150 C330,82 296,28 256,0 Z"
            fill="var(--leaf-green)"/>
    </svg>

    <section class="side-panel panel-usage">
      <div class="fine-print">
        <p>Mundöl zur Pflege des Mund-<br>raums</p>
        <p>Vor Gebrauch gut schütteln</p>
        <p>Anwendung:<br>Geben Sie je nach Belieben bis<br>maximal 4 Tropfen täglich mit der<br>beigefügten Pipette in die Mund-<br>höhle und belassen Sie das<br>Mundöl dort etwa eine<br>Minute, danach ausspucken. Ein<br>Verschlucken des Öles ist nicht<br>gesundheitsschädlich.</p>
      </div>
    </section>

    <section class="side-panel panel-info">
      <div class="fine-print">
        <p>Ingredients:<br>Cananbis sativa Seed Oil*,<br>Cannabis sativa Leaf Extract*,<br>Lecithin<br>*aus kontrollierter Bio-Produkti-<br>on</p>
        <p>Hinweis:<br>Außerhalb der Reichweite von<br>kleinen Kindern und Jugendli-<br>chen unter 18 Jahren aufbewah-<br>ren.<br>Nicht anwenden während der<br>Schwangerschaft und Stillzeit.</p>
        <p>Achtung:<br>Dieses Produkt beinhaltet<br>CBD/CBDA</p>
      </div>
      <div class="barcode-slot">Barcode</div>
    </section>

    <section class="side-panel panel-front">
      <div class="front-title">
        <div class="brand">XX</div>
        <div class="claim">Natürlich<br>schützend<br>und<br>regenerierend</div>
      </div>
    </section>

    <section class="side-panel panel-back">
      <div class="fine-print">
        <p>Das 'XX' Mundöl schützt und<br>regeneriert durch seinen pflegen-<br>den Komplex aus kaltgepresstem<br>Bio-Hanfsamenöl, mit seinen<br>wertvollen Omega 3, 6 und 9<br>Fettsäuren, sowie den natürlichen<br>Cannabinoiden wie<br>Cannabidiol (CBD) sowie dem<br>enthaltenen Lecithin die Mund-<br>schleimhaut und unterstützt diese<br>in ihrer natürlichen<br>Funktion als Schutzbarriere vor<br>schädlichen Umwelteinflüssen.</p>
      </div>
    </section>
  </div>
</body>
</html>
```